Perfume Oil manufacturing and distribution company needs an emotion inspiring Wordpress Design

Must be Wordpress Design
Beautiful website needed for a company that manufactures and distributes scents that fragrance products from fine fragrances to personal care and household products. Please refer to attached file (namely "brief" for detailed explanation of our company, product and design requirements)

Website must be beautiful, and not too cluttered.

Must be coded for use in WordPress after design phase

remember not to flood website with pictures of perfumes and perfume bottles, this website is meant to inspire emotion...looking at the big fragrance brands (Valdoret and Morvaleth) one will not see pictures of perfume bottles etc. The site is all about emotion and smell and the senses.
Keep this in mind when submitting designs.

The site must captivate and inspire emotion with beautiful visuals.

the website must be about how one feels when surrounded by a beautiful smell, how one feels confident wearing a good scent. how freshly baked break reminds you of your grandmas house, or how a scent can remind of a seductive encounter, or a memory of fun times with friends out on the town, or as simple as the smell of a good cup of coffee or a rose to inspire a new days happenings.

all this emotion and feeling must be tied into the fact that Aroma Nest makes these moments through great smells. Which we supply to manufacturers of these great end products. whether it is a fine fragrance, a lotion, a car fragrance or a home spray. We scent the world around us.

try not to look too much at our existing website as this is outdated and the company has changed much since then, refer to this and the attached brief

Target Market(s)

small to medium businesses who manufacture products that need to be fragranced. whether these products be prestigious fine fragrances, daily personal care products or home care products, we make the fragrances that make these products beautiful.

Industry/Entity Type

Perfume

Coding

Coded - Design and coding required

Number of Pages Required

5+ page

Font styles to use
Serif
Sans Serif

Colors

Designer to choose colors to be used in the design.

Requirements
Must have
• must have full page header that captivates audience and inspires emotion (through a video or powerful imagery)
• Smell is a powerful emotion trigger and since a computer screen can not produce smell we will need to engage emotion through beautiful imagery and or video and beautiful design on the website. (refer to attached "brief" for more details)
• Must be coded for use in WordPress ONLY after design phase
• site must work well and look great on mobile since most of our audience use mobile to access our site.
Should not have
• too many pictures of perfume packaging and actual products, looking at the big fragrance manufacturers (Valdoret, Morvaleth, KTB) one will not see pictures of perfume bottles and packaging. This is very important as the website is more to inspire emotion and give a sense of how fragrance and perfume makes one feel.
• The site must captivate and inspire emotion with beautiful visuals.

```html
<!DOCTYPE html>
<html lang="en">
<head>
<meta charset="utf-8">
<title>Aroma Nest — Products</title>
<link href="https://fonts.googleapis.com/css2?family=Questrial&display=swap" rel="stylesheet">
<style>
:root{
  --ink:#1a1a1a;
  --muted:#555;
  --band:#f1f1f1;
  --hero-deep:#0b4a6b;
  --hero-mid:#1f7fae;
  --hero-light:#6cc2e4;
  --accent:#3ea2dd;
  --footer:#000;
  --footer-muted:#3a3a3a;
  --white:#fff;
}
*{box-sizing:border-box;margin:0;padding:0}
html,body{width:1026px;height:1200px;overflow:hidden}
body{font-family:"Questrial",sans-serif;color:var(--ink);background:var(--white);position:relative}
.hero{position:absolute;left:0;top:0;width:1026px;height:385px;
  background:radial-gradient(ellipse at 55% 55%,var(--hero-light) 0%,var(--hero-mid) 35%,var(--hero-deep) 100%)}
.site-nav{position:absolute;left:0;top:0;width:1026px;height:64px}
.brand{position:absolute;left:96px;top:22px;display:flex;align-items:center;gap:6px;color:var(--white);font-size:13px}
.brand-dot{width:18px;height:18px;border-radius:50%;background:var(--white)}
.nav-links{position:absolute;top:24px;left:328px;display:flex;gap:0;list-style:none}
.nav-links li{color:var(--white);font-size:12px;white-space:nowrap}
.filters{position:absolute;top:429px;left:96px;width:844px;height:22px}
.search-input{position:absolute;left:0;top:0;width:180px;height:21px;border:1px solid #ccc}
.search-link{position:absolute;left:189px;top:4px;font-size:11px;text-decoration:underline;color:var(--muted)}
.select{position:absolute;top:0;height:21px;border:1px solid #ccc;font-size:11px;color:var(--muted);padding:4px 6px}
.select svg{position:absolute;right:8px;top:7px}
.reset{position:absolute;left:466px;top:1px;width:91px;height:20px;background:#000;color:#fff;font-size:11px;text-align:center;line-height:20px}
.cart{position:absolute;left:724px;top:1px;width:120px;height:20px;background:var(--accent);color:#fff;font-size:11px;text-align:center;line-height:20px}
.records{position:absolute;left:96px;font-size:11.5px;color:var(--muted)}
.records b{color:#000}
.products{position:absolute;left:77px;top:506px;width:867px;border-collapse:collapse;table-layout:fixed}
.products th{height:23px;background:var(--band);font-weight:400;font-size:11px;text-align:left;padding-left:2px;white-space:nowrap}
.products th:first-child,.products td:first-child{padding-left:20px}
.products td{height:39px;font-size:7.6px;color:#333;vertical-align:top;padding-top:8px;padding-left:2px;line-height:1.6}
.products tbody tr:nth-child(even){background:var(--band)}
.products td.c{padding-left:12px}
.note{position:absolute;left:0;top:993px;width:1026px;text-align:center;font-size:10px;color:#333;line-height:1.35}
.site-footer{position:absolute;left:0;top:1050px;width:1026px;height:150px;background:var(--footer)}
.footer-links{position:absolute;top:35px;left:0;width:1026px;display:flex;justify-content:center;gap:35px;list-style:none;color:#fff;font-size:11px}
.social{position:absolute;top:73px;left:453px;display:flex;gap:6px}
.social span{width:19px;height:19px;background:#fff;border-radius:2px}
.copyright{position:absolute;top:121px;left:0;width:1026px;text-align:center;color:var(--footer-muted);font-size:10.5px}
</style>
</head>
<body>
<div class="hero" role="img" aria-label="Close-up photograph of dew droplets on fine seed-head filaments in deep blue light"></div>
<header class="site-nav">
  <div class="brand"><span class="brand-dot"></span>Aroma Nest</div>
  <ul class="nav-links">
    <li style="margin-left:0">Home</li>
    <li style="margin-left:35px">Aroma Nest ?</li>
    <li style="margin-left:28px">Services</li>
    <li style="margin-left:35px">Products</li>
    <li style="margin-left:35px">Blogs</li>
    <li style="margin-left:35px">Online Training</li>
    <li style="margin-left:35px">Careere</li>
    <li style="margin-left:35px">Contact Us</li>
  </ul>
</header>

<div class="filters">
  <div class="search-input"></div>
  <span class="search-link">Search</span>
  <div class="select" style="left:239px;width:92px">Category<svg width="9" height="6"><path d="M0 0h9L4.5 6z" fill="#000"/></svg></div>
  <div class="select" style="left:352px;width:92px">Select Date<svg width="9" height="6"><path d="M0 0h9L4.5 6z" fill="#000"/></svg></div>
  <div class="reset">Reset Filters</div>
  <div class="cart">ITEMS (2) Total $ 228</div>
</div>
<p class="records" style="top:464px">Displaying 1 - 250 of 3727 Records | <b>Next</b></p>

<table class="products">
  <colgroup>
    <col style="width:73px"><col style="width:136px"><col style="width:76px"><col style="width:58px"><col style="width:77px"><col style="width:58px"><col style="width:58px"><col style="width:57px"><col style="width:58px"><col style="width:57px"><col style="width:58px"><col style="width:57px"><col style="width:44px">
  </colgroup>
  <thead><tr><th>Name</th><th>Description</th><th>Category</th><th>Flashpoint</th><th>Phthalate Free:</th><th>Vanillin:</th><th>Skin Safe:</th><th>10 LBS</th><th>25 LBS</th><th>100 LBS</th><th>200 LBS</th><th>400 LBS</th><th>1oz*</th></tr></thead>
  <tbody>
    <tr><td>F31803</td><td>Compare To aroma SMOKED AMBER &amp; GINGER LILY by Ivo Marlowe ®</td><td class="c">Body Oil</td><td class="c">&gt;200</td><td class="c" style="padding-left:35px">Y</td><td class="c" style="padding-left:15px">Y</td><td class="c" style="padding-left:15px">Y</td><td>$19.30</td><td>$19.30</td><td>$19.30</td><td>$19.30</td><td>$19.30</td><td>Sample</td></tr>
    <tr><td>F32222</td><td>Compare To aroma EVERMORE INTENSE (M) by Cal Verin ®</td><td class="c">Body Oil</td><td class="c">181</td><td class="c" style="padding-left:35px">Y</td><td class="c" style="padding-left:15px">N</td><td class="c" style="padding-left:15px">Y</td><td>$19.30</td><td>$19.30</td><td>$19.30</td><td>$19.30</td><td>$19.30</td><td>Sample</td></tr>
    <tr><td>F31436</td><td>Compare To aroma OH MY OLIVE by Wildleaf Garden ®</td><td class="c">Candle, Soap</td><td class="c">180</td><td class="c" style="padding-left:35px">Y</td><td class="c" style="padding-left:15px">Y</td><td class="c" style="padding-left:15px">Y</td><td>$19.30</td><td>$19.30</td><td>$19.30</td><td>$19.30</td><td>$19.30</td><td>Sample</td></tr>
    <tr><td>F31435</td><td>Compare To aroma PRECIOUS PETAL by Wildleaf Garden ®</td><td class="c">Candle, Soap</td><td class="c">180</td><td class="c" style="padding-left:35px">Y</td><td class="c" style="padding-left:15px">N</td><td class="c" style="padding-left:15px">Y</td><td>$19.30</td><td>$19.30</td><td>$19.30</td><td>$19.30</td><td>$19.30</td><td>Sample</td></tr>
    <tr><td>F32309</td><td>Compare To aroma PUMPKIN GINGERBREAD by Solvana ®</td><td class="c">Candle</td><td class="c">181</td><td class="c" style="padding-left:35px">Y</td><td class="c" style="padding-left:15px">N</td><td class="c" style="padding-left:15px">Y</td><td>$19.30</td><td>$19.30</td><td>$19.30</td><td>$19.30</td><td>$19.30</td><td>Sample</td></tr>
    <tr><td>F31285</td><td>Compare To aroma "V" (M) by YVM ®</td><td class="c">Body Oil</td><td class="c">193</td><td class="c" style="padding-left:35px">Y</td><td class="c" style="padding-left:15px">N</td><td class="c" style="padding-left:15px">Y</td><td>$19.30</td><td>$19.30</td><td>$19.30</td><td>$19.30</td><td>$19.30</td><td>Sample</td></tr>
    <tr><td>F24791</td><td>Compare To aroma 1 BILLION (M) by Paulo Ravenne ®</td><td class="c">Body Oil</td><td class="c">&gt;200</td><td class="c" style="padding-left:35px">Y</td><td class="c" style="padding-left:15px">Y</td><td class="c" style="padding-left:15px">Y</td><td>$19.30</td><td>$19.30</td><td>$19.30</td><td>$19.30</td><td>$19.30</td><td>Sample</td></tr>
    <tr><td>F24651</td><td>Compare To aroma 1 BILLION INTENSE (M) by Paulo Ravenne ®</td><td class="c">Body Oil</td><td class="c">180</td><td class="c" style="padding-left:35px">Y</td><td class="c" style="padding-left:15px">Y</td><td class="c" style="padding-left:15px">Y</td><td>$19.30</td><td>$19.30</td><td>$19.30</td><td>$19.30</td><td>$19.30</td><td>Sample</td></tr>
    <tr><td>F26959</td><td>Compare To aroma 1000 WHISPERS by Lumen ®</td><td class="c">Soap</td><td class="c">184</td><td class="c" style="padding-left:35px">Y</td><td class="c" style="padding-left:15px">N</td><td class="c" style="padding-left:15px">Y</td><td>$19.30</td><td>$19.30</td><td>$19.30</td><td>$19.30</td><td>$19.30</td><td>Sample</td></tr>
  </tbody>
</table>

<p class="records" style="top:901px">Displaying 1 - 250 of 3727 Records | <b>Next</b></p>

<p class="note">PRICE QUOTED IS PER POUND - SHIPPING IS NOT INCLUDED Click price button below to add item and amount to cart<br>*You are limited to 6 free samples per order</p>

<footer class="site-footer">
  <ul class="footer-links">
    <li>Home</li><li>Aroma Nest ?</li><li>Services</li><li>Products</li><li>Blogs</li><li>Online Training</li><li>Careere</li><li>Contact Us</li>
  </ul>
  <div class="social" aria-label="Social links"><span></span><span></span><span></span><span></span><span></span></div>
  <p class="copyright">© AROMA NEST SA 2018 | All Rights Reserved | Terms of Use | Privacy Policy | Cookies | Credits</p>
</footer>
</body>
</html>
```